Email Signatures

I would like to create a new email signature for my team. The design will be the same for everyone, with only individual details such as name and email changing. You can also see our brand style on our website. https://www.tlmbespokehomes.com.au/

Target Market(s)

Clients for new builds or renovations

Industry/Entity Type

Construction

Colors

Designer to choose colors to be used in the design.

```html
<!DOCTYPE html>
<html lang="en">
<head>
<meta charset="utf-8">
<title>TLM Email Signature</title>
<link rel="stylesheet" href="https://fonts.googleapis.com/css2?family=Saira:wght@400;700&display=swap">
<style>
  :root {
    --page-bg: #ececec;
    --card-bg: #ffffff;
    --brand-green: #2fa84a;
    --deep-green: #0d6a2e;
    --ink: #1f1f1f;
    --logo-ink: #2b2b2b;
  }
  * { margin: 0; padding: 0; box-sizing: border-box; }
  html, body {
    width: 1200px; height: 1200px; overflow: hidden;
    background: var(--page-bg);
    font-family: "Saira", sans-serif;
  }
  .signature {
    position: absolute;
    left: 88px; top: 480px;
    width: 1025px; height: 239px;
    background: var(--card-bg);
    overflow: hidden;
  }
  .signature__band {
    position: absolute; left: 0; top: 0;
    width: 1025px; height: 120px;
  }
  .brand {
    position: absolute;
    left: 80px; top: 62px;
    height: 130px;
    display: flex; align-items: center; gap: 14px;
  }
  .brand__mark {
    width: 22px; height: 22px;
    background: var(--brand-green);
  }
  .brand__name {
    font-weight: 700;
    font-size: 108px;
    line-height: 1;
    letter-spacing: 4px;
    color: var(--logo-ink);
  }
  .person {
    position: absolute;
    left: 615px; top: 50px;
  }
  .person__name {
    font-weight: 700;
    font-size: 21px;
    letter-spacing: 1px;
    color: var(--deep-green);
    line-height: 1.1;
  }
  .person__role {
    font-weight: 400;
    font-size: 18px;
    color: var(--ink);
    line-height: 1.3;
  }
  .contacts {
    list-style: none;
    margin-top: 20px;
  }
  .contacts__item {
    display: flex; align-items: center; gap: 9px;
    font-size: 15.5px;
    color: var(--ink);
    height: 24px;
    letter-spacing: 0.3px;
  }
  .contacts__icon {
    width: 12px; height: 12px;
    fill: var(--deep-green);
    flex: none;
  }
</style>
</head>
<body>
  <section class="signature">
    <svg class="signature__band" viewBox="0 0 1025 120" aria-hidden="true">
      <polygon points="256,0 1025,0 1025,29 521,29 415,109" fill="var(--brand-green)"/>
    </svg>

    <div class="brand">
      <span class="brand__name">TLM</span>
      <span class="brand__mark"></span>
    </div>

    <div class="person">
      <p class="person__name">DEAN MARLOW</p>
      <p class="person__role">General Manager</p>
      <ul class="contacts">
        <li class="contacts__item">
          <svg class="contacts__icon" viewBox="0 0 24 24"><path d="M6.6 10.8a15.1 15.1 0 0 0 6.6 6.6l2.2-2.2a1 1 0 0 1 1-.25 11.4 11.4 0 0 0 3.6.57 1 1 0 0 1 1 1V20a1 1 0 0 1-1 1A17 17 0 0 1 3 4a1 1 0 0 1 1-1h3.5a1 1 0 0 1 1 1c0 1.25.2 2.45.57 3.57a1 1 0 0 1-.25 1z"/></svg>
          <span>0400 555 184</span>
        </li>
        <li class="contacts__item">
          <svg class="contacts__icon" viewBox="0 0 24 24"><rect x="2" y="5" width="20" height="14" rx="1"/><path d="M3 6l9 7 9-7" stroke="#fff" stroke-width="1.8" fill="none"/></svg>
          <span>info@tlmbespokehomes.com.au</span>
        </li>
        <li class="contacts__item">
          <svg class="contacts__icon" viewBox="0 0 24 24"><circle cx="12" cy="12" r="10"/><path d="M2 12h20M12 2c3 3 3 17 0 20M12 2c-3 3-3 17 0 20" stroke="#fff" stroke-width="1.6" fill="none"/></svg>
          <span>www.tlmbespokehomes.com.au</span>
        </li>
        <li class="contacts__item">
          <svg class="contacts__icon" viewBox="0 0 24 24"><path d="M12 1a8 8 0 0 0-8 8c0 6 8 14 8 14s8-8 8-14a8 8 0 0 0-8-8zm0 11a3 3 0 1 1 0-6 3 3 0 0 1 0 6z"/></svg>
          <span>Ashford Bay, Kestrel Coast</span>
        </li>
      </ul>
    </div>
  </section>
</body>
</html>
```